EPS Packaging Infographic

We need two infographics focus on EPS packaging.

I've attached the copy as well as some of our other infographics to give you an idea of our style.

```html
<!DOCTYPE html>
<html lang="en">
<head>
<meta charset="utf-8">
<title>PS Bans vs. Curbside Collection</title>
<link href="https://fonts.googleapis.com/css2?family=Roboto+Condensed:wght@400;700&family=Roboto:wght@300;400&display=swap" rel="stylesheet">
<style>
  :root {
    --brown: #5b2e1f;
    --olive: #737a30;
    --steel: #5f8aa3;
    --mauve: #a08b86;
    --amber: #f4a11f;
    --moss: #aaa333;
    --panel: #5f8ba5;
    --ink: #111111;
    --paper: #ffffff;
  }
  * { margin: 0; padding: 0; box-sizing: border-box; }
  html, body { width: 1010px; height: 1200px; overflow: hidden; background: var(--paper); }
  .infographic { position: relative; width: 1010px; height: 1200px; overflow: hidden; }
  .title {
    position: absolute; left: 26px; top: 26px;
    font-family: "Roboto Condensed", "Arial Narrow", sans-serif;
    font-weight: 700; font-size: 62px; line-height: 55px;
    color: var(--brown); letter-spacing: -0.5px;
  }
  .chart { position: absolute; left: 0; top: 0; width: 1010px; height: 1200px; }
  .chart .cond { font-family: "Roboto Condensed", "Arial Narrow", sans-serif; }
  .chart .light { font-family: "Roboto", Arial, sans-serif; font-weight: 300; }
  .facts {
    position: absolute; left: 0; top: 845px; width: 815px; height: 224px;
    background: var(--panel); border-radius: 0 22px 22px 0;
    color: var(--paper); font-family: "Roboto", Arial, sans-serif; font-weight: 300;
    font-size: 19px; padding: 16px 10px 0 42px;
  }
  .facts ul { list-style: none; }
  .facts li { position: relative; line-height: 31.5px; }
  .facts li::before {
    content: ""; position: absolute; left: -21px; top: 13px;
    width: 7px; height: 7px; border-radius: 50%; background: var(--paper);
  }
  .facts p { line-height: 23.5px; margin-top: 1px; white-space: nowrap; }
  .reference {
    position: absolute; left: 22px; top: 1101px;
    font-family: "Roboto", Arial, sans-serif; font-size: 17.5px; line-height: 23px; color: var(--ink);
  }
</style>
</head>
<body>
<main class="infographic">
  <h1 class="title">PS BANS VS.<br>CURBSIDE COLLECTION</h1>

  <svg class="chart" viewBox="0 0 1270 1509" aria-label="Donut chart of the five states with the most EPS ordinances">
    <defs>
      <filter id="segment-shadow" x="-10%" y="-10%" width="130%" height="130%">
        <feDropShadow dx="4" dy="4" stdDeviation="5" flood-color="#000" flood-opacity="0.3"/>
      </filter>
    </defs>
    <g class="segments" filter="url(#segment-shadow)">
      <path fill="var(--moss)" d="M660.2,842.1 A287,287 0 0 1 460.2,806 L530.7,688.6 A150,150 0 0 0 635.3,707.5 Z"/>
      <path fill="var(--amber)" d="M719.4,822.5 A285,285 0 0 1 659.9,840.2 L635.3,707.5 A150,150 0 0 0 666.7,698.2 Z"/>
      <path fill="var(--mauve)" d="M861.9,689.4 A285,285 0 0 1 719.4,822.5 L666.7,698.2 A150,150 0 0 0 741.7,628.1 Z"/>
      <path fill="var(--steel)" d="M876.1,620.9 A275,275 0 0 1 853,684.9 L741.7,628.1 A150,150 0 0 0 754.3,593.2 Z"/>
      <path fill="var(--olive)" d="M881,560 A273,273 0 0 1 874.2,620.5 L754.3,593.2 A150,150 0 0 0 758,560 Z"/>
      <path fill="var(--brown)" d="M455,814.5 A297,297 0 1 1 905,560 L758,560 A150,150 0 1 0 530.7,688.6 Z"/>
    </g>

    <text class="cond" x="533" y="382" text-anchor="middle" font-size="46" font-weight="700" fill="#fff">California</text>
    <text class="cond" x="766" y="720" text-anchor="middle" font-size="17" font-weight="700" fill="#fff">MASSACHUSETTS</text>
    <text class="cond" x="570" y="767" text-anchor="middle" font-size="28" font-weight="700" fill="#fff">REST OF</text>
    <text class="cond" x="570" y="799" text-anchor="middle" font-size="28" font-weight="700" fill="#fff">THE US</text>

    <g class="center-label cond" text-anchor="middle" fill="var(--ink)">
      <text x="611" y="534" font-size="27">THE FIVE STATES</text>
      <text x="611" y="566" font-size="27">WITH THE MOST EPS</text>
      <text x="611" y="599" font-size="27">ORDINANCES</text>
      <text x="613" y="620" font-size="14">SOURCE: DANA R. ELLISON</text>
    </g>

    <g class="callouts" fill="none" stroke="var(--ink)" stroke-width="2.2">
      <line x1="242" y1="460" x2="330" y2="460"/>
      <polyline points="875,593 1019,593 1019,548"/>
      <line x1="858" y1="664" x2="1022" y2="664"/>
      <line x1="808" y1="767" x2="906" y2="767"/>
      <line x1="318" y1="830" x2="515" y2="830"/>
      <polyline points="480,921 693,921 693,820"/>
      <circle cx="190" cy="460" r="51" fill="#fff"/>
      <circle cx="1071" cy="548" r="51" fill="#fff"/>
      <circle cx="1072" cy="664" r="51" fill="#fff"/>
      <circle cx="956" cy="767" r="51" fill="#fff"/>
      <circle cx="267" cy="830" r="51" fill="#fff"/>
      <circle cx="430" cy="922" r="51" fill="#fff"/>
    </g>

    <g class="values light" text-anchor="middle" font-size="60" fill="var(--ink)">
      <text x="190" y="482">97</text>
      <text x="1071" y="570">5</text>
      <text x="1072" y="686">6</text>
      <text x="956" y="789">15</text>
      <text x="267" y="852">16</text>
      <text x="430" y="944">7</text>
    </g>

    <g class="state-labels light" font-size="28" fill="var(--ink)">
      <text x="960" y="588" text-anchor="middle">MAINE</text>
      <text x="948" y="692" text-anchor="middle">NEW YORK</text>
      <text x="487" y="917">FLORIDA</text>
    </g>
  </svg>

  <section class="facts">
    <ul>
      <li>Nearly 300 drop off locations</li>
      <li>82 Curbside programs</li>
      <li>More than 50 special collection Events/Year</li>
      <li>20 National mail bank locations</li>
    </ul>
    <p>146 Local governments-counties, cities, and towns - in15 states, including the district<br>of columbia, that have adopted ordinances to reduce or eliminate the consumption of<br>food service EPS. These orinances covered 6.8 percent of the U.S. population.</p>
  </section>

  <footer class="reference">
    Reference:<br>
    https://materials-loop.org/plastic/2016/12/08/rise-eps-ordinances
  </footer>
</main>
</body>
</html>
```